Modern Website Template

We need a set of modern website templates and would like to see what you can come up with.

The template should be easily customizable by an end user so they can easily swap out generic images with their own image if needed.

Some examples of templates you can create would be;
Small Business
Lawyer
Teacher
Birthday Party
Real Estate Agent
Doctor
Travel
Sports
Wedding
Religious

If we like your work we will be looking for more templates to be created.

**TEMPLATE MUST BE ORIGINAL AND NOT RESOLD**

Industry/Entity Type

Business

```html
<!DOCTYPE html>
<html lang="en">
<head>
<meta charset="utf-8">
<title>CareSphere – Connecting Your Health with the Future</title>
<link href="https://fonts.googleapis.com/css2?family=PT+Sans:wght@400;700&family=Arvo:wght@700&family=Arimo:wght@400;700&display=swap" rel="stylesheet">
<style>
:root{
  --paper:#ebe6da;
  --paper-light:#f3efe6;
  --panel:#ddd3c3;
  --green:#7fa82b;
  --green-dark:#5f8a1a;
  --green-light:#a9c94a;
  --brown:#6b3c16;
  --brown-text:#5a3412;
  --grey-text:#6b6660;
  --link:#6f9d1e;
  --dark-ui:#3b4246;
  --white:#ffffff;
}
*{box-sizing:border-box;margin:0;padding:0}
html,body{width:1200px;height:900px;overflow:hidden}
body{background:var(--paper);font-family:"Arimo",Arial,sans-serif;position:relative;color:var(--grey-text)}
.abs{position:absolute}

.top-rule{left:0;top:0;width:1200px;height:2px;background:linear-gradient(90deg,var(--brown) 0 376px,var(--green) 376px 816px,var(--green-light) 816px)}
.login-tab{left:997px;top:0;width:88px;height:30px;background:var(--paper-light);box-shadow:0 2px 4px rgba(0,0,0,.2);font:12px "Arimo",sans-serif;color:var(--brown);display:flex;align-items:center;padding-left:16px;gap:6px}
.login-tab i{width:12px;height:10px;background:var(--green);display:block;border-left:3px solid var(--brown)}

.brand{left:106px;top:58px;font:700 37px/1 "PT Sans",sans-serif;color:var(--green);letter-spacing:-1px}
.main-nav{right:113px;top:77px;display:flex;gap:20px;font:14px "PT Sans",sans-serif;text-transform:uppercase;color:var(--brown)}

.hero{left:0;top:136px;width:1200px;height:348px;background:radial-gradient(ellipse at 60% 40%,#9cc43c 0%,var(--green) 55%,#6a9522 100%)}
.zig{left:0;width:1200px;height:8px;background-size:10px 8px}
.zig-top{top:130px;background-image:linear-gradient(135deg,var(--paper) 50%,transparent 50%),linear-gradient(225deg,var(--paper) 50%,transparent 50%);background-color:var(--green)}
.zig-bottom{top:484px;background-image:linear-gradient(45deg,var(--paper) 50%,transparent 50%),linear-gradient(315deg,var(--paper) 50%,transparent 50%);background-color:#6d9823}

.video-frame{left:108px;top:165px;width:546px;height:290px;background:#f6f3ec;box-shadow:0 6px 14px rgba(0,0,0,.35)}
.video-photo{left:121px;top:176px;width:520px;height:268px;background:linear-gradient(180deg,#3f7fd0 0%,#8ab8ea 45%,#c9613e 70%,#2e4a2a 100%)}
.video-thumb{left:131px;top:185px;width:50px;height:50px;border:1px solid #fff;background:linear-gradient(135deg,#8ab8ea,#e0a83a)}
.video-title{left:186px;top:185px;width:162px;height:28px;background:rgba(40,46,50,.85);color:var(--green-light);font:700 16px/28px "PT Sans",sans-serif;padding-left:6px}
.video-from{left:186px;top:215px;width:110px;height:21px;background:rgba(40,46,50,.85);color:#fff;font:12px/21px "PT Sans",sans-serif;padding-left:6px}
.video-from span{color:var(--green-light)}
.video-action{left:588px;width:44px;height:36px;background:var(--dark-ui);border-radius:4px;color:#fff;font:700 9px "Arimo",sans-serif;text-align:center;padding-top:21px}
.video-action svg{position:absolute;left:14px;top:5px}
.play-btn{left:131px;top:394px;width:65px;height:38px;background:var(--dark-ui);border-radius:4px 4px 0 0}
.progress{left:206px;top:402px;width:414px;height:30px;background:var(--dark-ui);border-radius:4px 4px 0 0}
.progress-track{left:216px;top:412px;width:335px;height:11px;border:1px solid #9aa;background:#2d3336}
.progress-fill{left:218px;top:414px;width:130px;height:7px;background:var(--green-light)}
.volume{left:558px;top:411px;display:flex;gap:2px}
.volume i{width:3px;height:12px;background:var(--green-light);display:block}

.hero-title{left:686px;top:184px;font:700 30px/42px "Arvo",serif;color:#fff;letter-spacing:1px;text-shadow:2px 2px 2px rgba(0,0,0,.4)}
.hero-copy{left:689px;top:282px;width:390px;font:12.5px/22px "Arimo",sans-serif;color:#fff;text-shadow:1px 1px 1px rgba(0,0,0,.3)}
.cta{left:709px;top:396px;width:167px;height:55px;background:linear-gradient(#fbf8f1,#e4ddcf);box-shadow:0 3px 6px rgba(0,0,0,.3);font:700 18px/55px "PT Sans",sans-serif;color:var(--brown);text-align:center}

.section-tab{top:533px;width:227px;height:44px;background:linear-gradient(#f8f5ee,#e6e0d3);box-shadow:0 3px 5px rgba(0,0,0,.15);font:18px/44px "PT Sans",sans-serif;color:var(--brown);padding-left:22px}
.section-tab span{color:var(--green-dark)}

.thumb{width:83px;height:75px;background:#fff;box-shadow:0 2px 5px rgba(0,0,0,.25);padding:5px}
.thumb div{width:100%;height:100%}
.item-title{font:700 14px "Arimo",sans-serif;color:var(--brown-text)}
.item-text{width:210px;font:12.5px/18px "Arimo",sans-serif;color:var(--grey-text)}

.comment-panel{left:441px;top:605px;width:311px;height:300px;background:var(--panel);border-radius:6px}
.panel-links{left:666px;top:614px;font:11px "Arimo",sans-serif;color:var(--brown)}
.panel-links u{color:var(--brown)}
.panel-links b{font-weight:400;color:var(--link);text-decoration:underline}

.news-title{left:782px;font:700 14px "Arimo",sans-serif;color:var(--brown-text)}
.news-text{left:782px;width:300px;font:12.5px/18px "Arimo",sans-serif;color:var(--grey-text)}
.news-meta{left:782px;font:11px "Arimo",sans-serif;color:var(--brown-text)}
.news-meta span{color:var(--link)}
.news-rule{left:782px;width:310px;height:1px;background:#d8d0c2}
</style>
</head>
<body>
<div class="abs top-rule"></div>
<div class="abs login-tab"><i></i>Login</div>

<header>
  <div class="abs brand">CareSphere</div>
  <nav class="abs main-nav"><span>Home</span><span>Our Patients</span><span>Services</span><span>News</span><span>Blog</span><span>Centers</span><span>Directories</span><span>Contact</span></nav>
</header>

<section class="hero-band">
  <div class="abs hero"></div>
  <div class="abs zig zig-top"></div>
  <div class="abs zig zig-bottom"></div>

  <div class="abs video-frame"></div>
  <div class="abs video-photo" role="img" aria-label="Video still: mother and daughter with outstretched arms under a blue sky"></div>
  <div class="abs video-thumb" role="img" aria-label="Channel thumbnail with a paper pinwheel"></div>
  <div class="abs video-title">Health Virtual Tour</div>
  <div class="abs video-from">from <span>CareSphere</span></div>
  <div class="abs video-action" style="top:186px"><svg width="16" height="14" viewBox="0 0 16 14"><path d="M8 13 1.5 6.5A3.6 3.6 0 0 1 8 2a3.6 3.6 0 0 1 6.5 4.5Z" fill="#fff"/></svg>LIKE</div>
  <div class="abs video-action" style="top:226px"><svg width="16" height="14" viewBox="0 0 16 14"><path d="M2 12 12 2M7 2h5v5" stroke="#fff" stroke-width="2" fill="none"/></svg>SHARE</div>
  <div class="abs video-action" style="top:266px"><svg width="16" height="14" viewBox="0 0 16 14"><path d="M5 3 1 7l4 4M11 3l4 4-4 4M9 2 7 12" stroke="#fff" stroke-width="1.8" fill="none"/></svg>EMBED</div>
  <div class="abs play-btn"><svg class="abs" style="left:25px;top:11px" width="16" height="17" viewBox="0 0 16 17"><path d="M1 1l14 7.5L1 16Z" fill="#fff"/></svg></div>
  <div class="abs progress"></div>
  <div class="abs progress-track"></div>
  <div class="abs progress-fill"></div>
  <div class="abs volume"><i></i><i></i><i></i><i></i><i></i><i></i><i></i><i></i></div>
  <svg class="abs" style="left:600px;top:411px" width="12" height="12" viewBox="0 0 12 12"><path d="M1 1l4 4M11 1 7 5M1 11l4-4M11 11 7 7" stroke="#fff" stroke-width="2"/></svg>

  <h1 class="abs hero-title">Connecting Your Health<br>with the Future</h1>
  <p class="abs hero-copy">Imperdiet sed est. Quisque suscipit nisi ac turpis mollis et sollicitudin tellus vehicula. Maecenas justo eros, tincidunt eu porttitor sed, imper­diet vel est. Cras a lorem metus. Donec pharetra, orci quis sagittis feugiat, tortor mi molestie quam.</p>
  <div class="abs cta">START NOW!</div>
</section>

<section class="column-health">
  <h2 class="abs section-tab" style="left:105px;font-weight:400">Health <span>Title 1</span></h2>
  <div class="abs thumb" style="left:106px;top:618px"><div role="img" aria-label="Photo of trees under a cloudy sky" style="background:linear-gradient(#7d9bb8,#c9d3dc 60%,#4f7a2a)"></div></div>
  <div class="abs item-title" style="left:205px;top:622px">Subtitle 1</div>
  <div class="abs item-text" style="left:205px;top:646px">Lorem ipsum dolor sit amet, consecte-tur adipiscing elit. Quisque euismod</div>
  <div class="abs thumb" style="left:106px;top:722px"><div role="img" aria-label="Photo of white pills and orange capsules" style="background:linear-gradient(135deg,#5fb6c4,#e8eef0 50%,#e08a3a)"></div></div>
  <div class="abs item-title" style="left:205px;top:726px">Subtitle 2</div>
  <div class="abs item-text" style="left:205px;top:750px">Lorem ipsum dolor sit amet, consecte-tur adipiscing elit. Quisque euismod</div>
  <div class="abs thumb" style="left:106px;top:825px"><div role="img" aria-label="Photo of crayons beside white puzzle pieces" style="background:linear-gradient(90deg,#c8553a,#e7e2d8 30%,#f2efe8)"></div></div>
  <div class="abs item-title" style="left:205px;top:829px">Subtitle 3</div>
  <div class="abs item-text" style="left:205px;top:853px">Lorem ipsum dolor sit amet, consecte-tur adipiscing elit. Quisque euismod</div>
</section>

<section class="column-comments">
  <h2 class="abs section-tab" style="left:442px;font-weight:400">Health <span>Title 2</span></h2>
  <div class="abs comment-panel"></div>
  <div class="abs panel-links">• <u>Forum</u> &nbsp;<b>• Blog</b></div>
  <div class="abs thumb" style="left:453px;top:628px"><div role="img" aria-label="User avatar" style="background:linear-gradient(#e6e6e6,#b9c4c9)"></div></div>
  <div class="abs item-title" style="left:552px;top:632px">User Comment</div>
  <div class="abs item-text" style="left:552px;top:656px;width:190px">“Lorem ipsum dolor sit amet, dolor consectetur adipiscing elit nam eu”</div>
  <div class="abs thumb" style="left:453px;top:732px"><div role="img" aria-label="User avatar" style="background:linear-gradient(#e6e6e6,#3f7a3a)"></div></div>
  <div class="abs item-title" style="left:552px;top:736px">User Comment</div>
  <div class="abs item-text" style="left:552px;top:760px;width:190px">“Lorem ipsum dolor sit amet, dolor consectetur adipiscing elit nam eu”</div>
  <div class="abs thumb" style="left:453px;top:835px"><div role="img" aria-label="User avatar" style="background:linear-gradient(#e6e6e6,#d9b83c)"></div></div>
  <div class="abs item-title" style="left:552px;top:839px">User Comment</div>
  <div class="abs item-text" style="left:552px;top:863px;width:190px">“Lorem ipsum dolor sit amet, dolor consectetur adipiscing elit nam eu”</div>
</section>

<section class="column-news">
  <h2 class="abs section-tab" style="left:782px;font-weight:400">Health <span>News</span></h2>
  <div class="abs news-title" style="top:610px">News Title 1 Goes Here</div>
  <div class="abs news-text" style="top:635px">Im ipsum dolor sit amet, dolor consectetur adipiscing lorem lipsm dolor sit mani nisi tyrrpis sagitis set.</div>
  <div class="abs news-meta" style="top:677px">• 36 people like this <span>• view user comments</span></div>
  <div class="abs news-rule" style="top:700px"></div>
  <div class="abs news-title" style="top:714px">News Title 2 Goes Here</div>
  <div class="abs news-text" style="top:739px">Im ipsum dolor sit amet, dolor consectetur adipiscing lorem lipsm dolor sit mani nisi tyrrpis sagitis set.</div>
  <div class="abs news-meta" style="top:781px">• 36 people like this <span>• view user comments</span></div>
  <div class="abs news-rule" style="top:804px"></div>
  <div class="abs news-title" style="top:818px">News Title 3 Goes Here</div>
  <div class="abs news-text" style="top:843px">Im ipsum dolor sit amet, dolor consectetur adipiscing lorem lipsm dolor sit mani nisi tyrrpis sagitis set.</div>
  <div class="abs news-meta" style="top:885px">• 36 people like this <span>• view user comments</span></div>
</section>
</body>
</html>
```